business cards for heating company

I need business cards for my heating air conditioning and chimney company located in upstate NY I would like for them to be colorful and catchy on heavy stock with preferably a glossy finish on front of card but the ability to write something on one half of the back with maybe some bullets on the other half of the back I also need to be able to change the name and title of employees on the card and also incorporate some of our current look and feel from our trucks and website I also want to be able to use this design or similar to have door hangers made lawn signs coffee mugs key chains etc. our website is Brindlecove.com

Target Market(s)

homeowners

Industry/Entity Type

Air Conditioning

Contact Information for Business Card

should have website brindlecove.com , phone number 585-437-9168 please look at website for ideas

Font styles to use
Sans Serif

Colors
ec1f27
3176b5
fbee3f

Requirements
Must have
• a complete look
Nice to have
• a discount offer like 10% military and first responders
• senior discount %5

```html
<!DOCTYPE html>
<html lang="en">
<head>
<meta charset="utf-8">
<title>Brindle Cove – Business Card</title>
<link rel="stylesheet" href="https://fonts.googleapis.com/css2?family=Lato:wght@300;400;700;900&display=swap">
<style>
  :root {
    --bg: #efebe5;
    --pink: #c73a6c;
    --pink-light: #d95586;
    --pink-dark: #a82c58;
    --blue: #2e8fd6;
    --white: #ffffff;
    --paper: #f6f6f6;
    --rule: #c94b78;
  }
  * { box-sizing: border-box; margin: 0; padding: 0; }
  html, body { width: 1200px; height: 600px; overflow: hidden; }
  body {
    background: var(--bg);
    font-family: "Lato", Arial, sans-serif;
    display: flex; align-items: center; justify-content: center; gap: 60px;
  }
  .card {
    position: relative; width: 520px; height: 297px; overflow: hidden;
    box-shadow: 0 6px 18px rgba(0,0,0,.18);
  }

  /* Front */
  .card--front {
    background: linear-gradient(135deg, var(--pink-light) 0%, var(--pink) 45%, var(--pink-dark) 100%);
    color: var(--white);
  }
  .brand { position: absolute; left: 34px; top: 30px; }
  .brand__name { font-weight: 900; font-size: 34px; letter-spacing: .5px; line-height: 1; text-transform: uppercase; }
  .brand__tagline { font-weight: 400; font-size: 15.5px; letter-spacing: .6px; margin-top: 4px; text-transform: uppercase; }
  .person { position: absolute; left: 150px; top: 128px; text-align: center; }
  .person__name { font-weight: 700; font-size: 13px; letter-spacing: 1px; text-transform: uppercase; }
  .person__name span { color: #8fd0ff; }
  .person__title { font-weight: 400; font-size: 10.5px; margin-top: 3px; }
  .divider { position: absolute; left: 34px; right: 34px; top: 196px; height: 1.5px; background: var(--white); }
  .contact { position: absolute; left: 34px; top: 212px; list-style: none; font-size: 11px; line-height: 17px; font-weight: 300; }
  .contact li { display: flex; align-items: center; gap: 7px; }
  .contact__mark { width: 11px; height: 11px; border-radius: 2px; background: var(--blue); flex: none; }
  .office { position: absolute; right: 34px; top: 212px; text-align: right; font-size: 11px; line-height: 17px; font-weight: 300; }
  .office__label { font-weight: 700; }

  /* Back */
  .card--back { background: var(--paper); }
  .back__side {
    position: absolute; left: 0; top: 0; bottom: 0; width: 150px;
    background: linear-gradient(160deg, var(--pink-light), var(--pink-dark));
    color: var(--white); padding: 26px 14px;
  }
  .back__side .brand__name { font-size: 19px; }
  .back__side .brand__tagline { font-size: 8.5px; margin-top: 3px; }
  .back__side .contact { position: static; margin-top: 118px; font-size: 9px; line-height: 14px; }
  .back__side .contact__mark { width: 9px; height: 9px; }
  .appointment__header {
    position: absolute; left: 150px; right: 0; top: 0; height: 34px;
    background: var(--pink); color: var(--white);
    font-weight: 700; font-size: 14px; text-align: right; padding: 9px 18px 0 0;
  }
  .appointment__lines { position: absolute; left: 176px; right: 26px; top: 58px; }
  .appointment__lines span { display: block; height: 1.3px; background: var(--rule); margin-bottom: 44px; }
  .appointment__note {
    position: absolute; left: 150px; right: 0; bottom: 0; height: 36px;
    background: var(--pink); color: var(--white);
    font-size: 9.5px; font-weight: 400; padding: 12px 0 0 16px;
  }
</style>
</head>
<body>
  <section class="card card--front" aria-label="Business card front">
    <div class="brand">
      <div class="brand__name">Brindle Cove</div>
      <div class="brand__tagline">Heating, Cooling &amp; Chimney</div>
    </div>
    <div class="person">
      <div class="person__name">Daniel <span>Whitaker</span></div>
      <div class="person__title">Managing Director</div>
    </div>
    <div class="divider"></div>
    <ul class="contact">
      <li><i class="contact__mark"></i>(585) 437-9168</li>
      <li><i class="contact__mark"></i>info@brindlecove.com</li>
      <li><i class="contact__mark"></i>brindlecove.com</li>
    </ul>
    <div class="office">
      <div class="office__label">Main Office:</div>
      <div>318 Alder Lane</div>
      <div>Walworth, NY 14568</div>
    </div>
  </section>

  <section class="card card--back" aria-label="Business card back">
    <div class="back__side">
      <div class="brand__name">Brindle Cove</div>
      <div class="brand__tagline">Heating, Cooling &amp; Chimney</div>
      <ul class="contact">
        <li><i class="contact__mark"></i>(585) 437-9168</li>
        <li><i class="contact__mark"></i>info@brindlecove.com</li>
        <li><i class="contact__mark"></i>brindlecove.com</li>
      </ul>
    </div>
    <div class="appointment__header">Next Appointment</div>
    <div class="appointment__lines"><span></span><span></span><span></span><span></span></div>
    <div class="appointment__note">Your appointment has been personally reserved for you. Late cancellation will usually incur a fee.</div>
  </section>
</body>
</html>
```